Maren's Atelier, Beauty & Therapy. New business in Verbier, Switzerland

Simple Flyer to put in evidence a particular service that the studio offers that is
EMS ( ELECTRIC MUSCLE STIMULATION)
There is a bike festival in Verbier ion the 12th of August and i would like to take an opportunity of this slot to advertise our new suit of EMS that can be very helpful for bike riders. The product is a suit with muscle electrostimulation, And there are many advantages and functionnality. For sportsmen and women, it can
I don't have any particular picture be cause the product is very new.
But i can send you some images for you to understand what it is, but if you find some images on the web it is better :)
I upload different versions of Logo, PLEASE FEEL FREE TO CHOOSE WHAT IS BEST :)
please check this link for more information about the product applied for bikers
https://www.pulsavo-fit.com/en/cycling-training-with-muscle-electrostimulation/
Updates
Hello Designers,
Here are a few details concerning the project;
- Maren's Atelier is not a reseller of the EMS suits, but we provide it as a service inside our studio.
- We wish to communicate on this new technology in order to bring a maximum of attention, not only for the suit, but also for the brand it self, since it is new in Verbier.
- for the flyer, i would like it to be simple, appealing, and without too much text.
- a french version of the same flyer is appreciated, without extra cost ;)
Thanks
Hello all designers,
thank you for all the good work.
For you who mentioned a date for the festival, i suggest please to take it off, and keep only " Alpenrad Pedal Days" if you want.
Thank you

```html
<!DOCTYPE html>
<html lang="en">
<head>
<meta charset="utf-8">
<title>Maren's Atelier – EMS Flyer</title>
<link rel="stylesheet" href="https://fonts.googleapis.com/css2?family=Montserrat:wght@400;500;700;800&display=swap">
<style>
  :root{
    --backdrop:#e7d9d2;
    --magenta:#9b2172;
    --plum:#6f1b58;
    --plum-deep:#5a1248;
    --cream:#fbece6;
    --white:#ffffff;
  }
  *{margin:0;padding:0;box-sizing:border-box}
  html,body{width:1200px;height:1200px;overflow:hidden;background:var(--backdrop)}
  body{font-family:'Montserrat',sans-serif}
  .flyer{position:absolute;left:200px;top:35px;width:800px;height:1130px;overflow:hidden;background:var(--plum);box-shadow:0 18px 40px rgba(80,40,50,.25)}
  .flyer-art{position:absolute;inset:0}
  .brand{position:absolute;left:290px;top:310px;width:220px;height:220px;border-radius:50%;display:flex;flex-direction:column;align-items:center;justify-content:center;text-align:center;color:var(--plum)}
  .brand-dot{width:20px;height:20px;border-radius:50%;background:var(--plum);margin-bottom:12px}
  .brand-name{font-weight:700;font-size:24px;letter-spacing:2px;text-transform:uppercase;line-height:1.15}
  .brand-tag{font-weight:700;font-size:13px;margin-top:8px;letter-spacing:.5px}
  .offer{position:absolute;left:0;right:0;top:572px;text-align:center;color:var(--white)}
  .offer-title{font-weight:800;font-size:40px;letter-spacing:1px;line-height:1}
  .offer-sub{font-weight:400;font-size:17px;letter-spacing:2px;margin-top:2px}
  .offer-service{font-weight:800;font-size:38px;line-height:1}
  .offer-full{font-weight:700;font-size:17px;margin-top:4px}
  .mission{position:absolute;left:40px;top:748px;width:400px;text-align:center;color:var(--white)}
  .mission-pill{display:inline-block;background:var(--cream);color:var(--plum);font-weight:800;font-size:28px;padding:5px 28px;border-radius:30px;margin-bottom:10px}
  .mission-text{font-size:15px;line-height:1.42}
  .mission-text strong{font-weight:700;font-size:21px}
  .contact{position:absolute;left:0;right:0;top:1020px;height:90px;background:var(--cream);color:var(--plum);display:flex;align-items:center;font-size:16px}
  .contact-address{flex:0 0 430px;display:flex;align-items:center;gap:8px;padding-left:40px}
  .contact-divider{width:2px;height:50px;background:var(--plum)}
  .contact-lines{padding-left:26px;display:flex;flex-direction:column;gap:8px}
  .contact-line{display:flex;align-items:center;gap:8px}
  .contact-icon{width:14px;height:14px;flex:none}
  .footer-strip{position:absolute;left:0;right:0;top:1110px;height:20px;background:var(--plum)}
</style>
</head>
<body>
<div class="flyer">
  <svg class="flyer-art" viewBox="0 0 800 1130" width="800" height="1130">
    <defs>
      <linearGradient id="photo-ems" x1="0" y1="0" x2="0" y2="1"><stop offset="0" stop-color="#f3f1f1"/><stop offset=".6" stop-color="#cfcdd0"/><stop offset="1" stop-color="#4a4750"/></linearGradient>
      <linearGradient id="photo-mountain" x1="0" y1="0" x2="0" y2="1"><stop offset="0" stop-color="#4f86cf"/><stop offset=".45" stop-color="#d4dee9"/><stop offset="1" stop-color="#6e6b5a"/></linearGradient>
      <linearGradient id="photo-meadow" x1="0" y1="0" x2="0" y2="1"><stop offset="0" stop-color="#eef1f3"/><stop offset=".3" stop-color="#93ad62"/><stop offset="1" stop-color="#5c9a36"/></linearGradient>
      <linearGradient id="photo-rider" x1="0" y1="0" x2="1" y2="0"><stop offset="0" stop-color="#c9b08e"/><stop offset=".5" stop-color="#9a4a42"/><stop offset="1" stop-color="#3b3033"/></linearGradient>
    </defs>
    <!-- faceted background around the diamond mosaic -->
    <rect width="800" height="1130" fill="var(--plum)"/>
    <polygon points="0,0 400,0 400,20 200,220" fill="var(--magenta)"/>
    <polygon points="0,0 200,220 0,420" fill="var(--plum)"/>
    <polygon points="800,0 400,0 400,20 600,220" fill="var(--plum)"/>
    <polygon points="800,0 600,220 800,420" fill="var(--magenta)"/>
    <polygon points="0,420 200,620 0,820" fill="var(--magenta)"/>
    <polygon points="800,420 600,620 800,820" fill="var(--plum-deep)"/>
    <polygon points="400,420 600,620 400,820 200,620" fill="var(--plum)"/>
    <polygon points="0,820 230,900 0,1020" fill="var(--magenta)"/>
    <!-- diamond photo tiles -->
    <polygon role="img" aria-label="Photo: people training in EMS suits" points="400,34 586,220 400,406 214,220" fill="url(#photo-ems)" stroke="var(--cream)" stroke-width="7" stroke-linejoin="round"/>
    <polygon role="img" aria-label="Photo: mountain biker riding up a rocky alpine slope" points="200,234 386,420 200,606 14,420" fill="url(#photo-mountain)" stroke="var(--cream)" stroke-width="7" stroke-linejoin="round"/>
    <polygon role="img" aria-label="Photo: two women exercising in EMS suits on a grassy hill" points="600,234 786,420 600,606 414,420" fill="url(#photo-meadow)" stroke="var(--cream)" stroke-width="7" stroke-linejoin="round"/>
    <rect role="img" aria-label="Photo: smiling cyclist carrying a road bike at sunset" x="470" y="770" width="296" height="226" fill="url(#photo-rider)" stroke="var(--cream)" stroke-width="8"/>
    <!-- brand circle -->
    <circle cx="400" cy="420" r="122" fill="var(--cream)" stroke="var(--plum)" stroke-width="10"/>
    <circle cx="400" cy="420" r="130" fill="none" stroke="var(--cream)" stroke-width="6"/>
  </svg>

  <div class="brand">
    <div class="brand-dot"></div>
    <div class="brand-name">Maren's<br>Atelier</div>
    <div class="brand-tag">Beauty &amp; Therapy</div>
  </div>

  <div class="offer">
    <div class="offer-title">OUR STUDIO</div>
    <div class="offer-sub">OFFERS</div>
    <div class="offer-service">EMS</div>
    <div class="offer-full">(ELECTRIC MUSCLE STIMULATION)</div>
  </div>

  <div class="mission">
    <div class="mission-pill">OUR MISSION</div>
    <p class="mission-text">is to help you feel better in your body and mind by providing you with quality treatments that are tailored to your needs and preferences. Whether you are looking to <strong>decompress</strong>,<strong>refresh yourself</strong>, or <strong>boost</strong> your <strong>energy</strong>, We are here to help you achieve your goals.</p>
  </div>

  <div class="contact">
    <div class="contact-address">
      <svg class="contact-icon" viewBox="0 0 14 14"><circle cx="7" cy="7" r="7" fill="var(--plum)"/><path d="M7 3.2a2.6 2.6 0 0 0-2.6 2.6C4.4 7.8 7 10.8 7 10.8s2.6-3 2.6-5A2.6 2.6 0 0 0 7 3.2z" fill="var(--cream)"/><circle cx="7" cy="5.8" r="1" fill="var(--plum)"/></svg>
      <span>Chemin des Mélèzes 14, Verbier, Suisse</span>
    </div>
    <div class="contact-divider"></div>
    <div class="contact-lines">
      <div class="contact-line">
        <svg class="contact-icon" viewBox="0 0 14 14"><circle cx="7" cy="7" r="7" fill="var(--plum)"/><path d="M4.6 3.6l1.3 1.6-.7.9c.5 1 1.3 1.8 2.3 2.3l.9-.7 1.6 1.3-.7 1.2C7 10 4 7 3.7 4.3z" fill="var(--cream)"/></svg>
        <span>+41-79 000 4817</span>
      </div>
      <div class="contact-line">
        <svg class="contact-icon" viewBox="0 0 14 14"><circle cx="7" cy="7" r="7" fill="var(--plum)"/><rect x="3.5" y="4.5" width="7" height="5" fill="var(--cream)"/><path d="M3.5 4.5L7 7.3l3.5-2.8" fill="none" stroke="var(--plum)" stroke-width=".9"/></svg>
        <span>hello@marensatelier.ch</span>
      </div>
    </div>
  </div>
  <div class="footer-strip"></div>
</div>
</body>
</html>
```